goal design

We are rolling out a goal for the next 3 years. the goal is as follows:
2014: $8 million gross profit, $1.25 million net income
2015: $12 million gross profit, $2.4 million net income
2016 $15 million gross profit, $4 million net income
We want a design that captures these numbers and that we can publish company wide that will quickly remind everyone of these goals. Our website is www.brookvalerecruiting.example. This will be an internal campaign. We will use the simple design to remind our people of our goals for the next 3 years. We will print it on mouse pads, shirts and things of this nature periodically to keep it front of mind for our people. So easy to remember, visually appealing and simple are good guidelines.
Updates
Target Market(s)
This is an internal campaign. it is to remind our people of our goals for the next few years so will be on little reminder items (i.e. cell phone covers, mouse pads, shirts, screen savers, etc).
Industry/Entity Type
It Company
Look and feel

```html
<!DOCTYPE html>
<html lang="en">
<head>
<meta charset="utf-8">
<title>Three-Year Goals — Brookvale Recruiting</title>
<link rel="stylesheet" href="https://fonts.googleapis.com/css2?family=Jost:wght@300;400;700;800&display=swap">
<style>
  :root {
    --navy: #143764;
    --navy-deep: #0e2c55;
    --bg-center: #ffffff;
    --bg-edge: #b9c6dd;
    --brand: #1f2a3a;
  }
  * { margin: 0; padding: 0; box-sizing: border-box; }
  html, body { width: 1200px; height: 1167px; overflow: hidden; }
  body { font-family: "Jost", "Helvetica Neue", Arial, sans-serif; color: var(--navy); }

  .goal-card {
    position: relative;
    width: 1200px;
    height: 1167px;
    background: radial-gradient(ellipse 75% 70% at 50% 52%, var(--bg-center) 0%, #f1f4f9 55%, #d7dfec 82%, var(--bg-edge) 100%);
    overflow: hidden;
  }

  .headline {
    position: absolute;
    top: 124px;
    left: 0;
    width: 1200px;
    text-align: center;
    font-size: 80px;
    line-height: 93px;
    font-weight: 400;
    letter-spacing: -0.5px;
  }
  .headline strong {
    display: block;
    font-weight: 800;
    color: var(--navy-deep);
    letter-spacing: -1px;
  }

  .goal-row {
    position: absolute;
    left: 140px;
    height: 120px;
    display: flex;
    align-items: center;
  }
  .goal-row--2014 { top: 442px; }
  .goal-row--2015 { top: 586px; }
  .goal-row--2016 { top: 730px; }

  .goal-year {
    width: 362px;
    flex: none;
    font-size: 156px;
    line-height: 120px;
    height: 120px;
    font-weight: 300;
    letter-spacing: -5px;
    color: var(--navy);
    white-space: nowrap;
  }
  .goal-year b { font-weight: 800; color: var(--navy-deep); }

  .goal-figures {
    padding-left: 6px;
    padding-top: 10px;
    font-size: 49px;
    line-height: 49px;
    font-weight: 300;
    white-space: nowrap;
  }
  .goal-figures b { font-weight: 700; color: var(--navy-deep); }

  .brand {
    position: absolute;
    top: 968px;
    left: 0;
    width: 1200px;
    display: flex;
    justify-content: center;
    align-items: center;
    gap: 16px;
  }
  .brand-dot {
    width: 30px;
    height: 30px;
    border-radius: 50%;
    background: var(--navy);
  }
  .brand-name {
    font-size: 40px;
    font-weight: 700;
    letter-spacing: 3px;
    text-transform: uppercase;
    color: var(--brand);
  }
</style>
</head>
<body>
  <main class="goal-card">
    <h1 class="headline">
      Our sense of urgency and<br>
      personalized solutions
      <strong>will set us apart</strong>
    </h1>

    <section class="goal-row goal-row--2014">
      <div class="goal-year">20<b>14</b></div>
      <div class="goal-figures">
        <div><b>$8 million</b> gross profit</div>
        <div><b>$1.25 million</b> net income</div>
      </div>
    </section>

    <section class="goal-row goal-row--2015">
      <div class="goal-year">20<b>15</b></div>
      <div class="goal-figures">
        <div><b>$12 million</b> gross profit</div>
        <div><b>$2.4 million</b> net income</div>
      </div>
    </section>

    <section class="goal-row goal-row--2016">
      <div class="goal-year">20<b>16</b></div>
      <div class="goal-figures">
        <div><b>$15 million</b> gross profit</div>
        <div><b>$4 million</b> net income</div>
      </div>
    </section>

    <footer class="brand">
      <span class="brand-dot"></span>
      <span class="brand-name">Brookvale Recruiting</span>
    </footer>
  </main>
</body>
</html>
```